Home Security Company Business Card

Looking for a eye catching business card that is non traditional and stands out but yet still looks professional. It should include all the pertinent information such as name, title, address, telephone, e-mail, website address should definitely stand out and then finally the logo.

Target Market(s)

Residential and Commercial accounts mostly upscale accounts

Industry/Entity Type

Security

Contact Information for Business Card

Name
Title
Address
Office #
Cell #
E-mail
Website

Font styles to use
Serif
Sans Serif

Requirements
Must have
• Logo, two sided color configuration
Nice to have
• You decide
Should not have
• There really aren't any.

```html
<!DOCTYPE html>
<html lang="en">
<head>
<meta charset="utf-8">
<title>Havenpoint Security Systems – Business Card</title>
<link href="https://fonts.googleapis.com/css2?family=Crimson+Pro:wght@400&family=Open+Sans:ital,wght@0,400;0,600;1,400&display=swap" rel="stylesheet">
<style>
  :root {
    --backdrop: #3c3c3c;
    --card-white: #fafafa;
    --brand-red: #7a0f04;
    --brand-red-light: #9a2410;
    --brand-gold: #d39a4a;
    --title-orange: #d98a2b;
    --body-grey: #4a4a4a;
    --rule-grey: #c9c9c9;
    --white: #ffffff;
  }
  * { margin: 0; padding: 0; box-sizing: border-box; }
  html, body {
    width: 1200px; height: 750px; overflow: hidden;
    background: var(--backdrop);
  }
  .canvas { position: relative; width: 1200px; height: 750px; }

  .card {
    position: absolute; top: 228px;
    width: 461px; height: 262px; overflow: hidden;
  }
  .card-front { left: 144px; background: var(--card-white); }
  .card-back  { left: 612px; }

  /* Front */
  .front-wave { position: absolute; left: 0; top: 0; width: 461px; height: 262px; }

  .brand-mark {
    position: absolute; left: 48px; top: 100px;
    display: flex; align-items: center; gap: 10px;
  }
  .brand-dot {
    width: 38px; height: 38px; border-radius: 50%;
    background: var(--brand-gold);
  }
  .brand-name {
    font-family: "Crimson Pro", serif; font-weight: 400;
    color: var(--brand-red); line-height: 1;
  }
  .brand-name .line-main { display: block; font-size: 21px; letter-spacing: 0.2px; }
  .brand-name .line-sub  { display: block; font-size: 9.5px; letter-spacing: 0.1px; margin-top: 2px; }

  .divider {
    position: absolute; left: 257px; top: 48px;
    width: 1px; height: 146px; background: var(--rule-grey);
  }

  .contact {
    position: absolute; left: 276px; top: 48px;
    font-family: "Open Sans", sans-serif; color: var(--body-grey);
  }
  .contact-name { font-size: 16px; font-weight: 600; color: var(--brand-red); line-height: 1.2; }
  .contact-title { font-size: 12px; color: var(--title-orange); line-height: 1.3; margin-bottom: 9px; }
  .contact-address { font-size: 10.5px; line-height: 14px; margin-bottom: 6px; }
  .contact-list { list-style: none; font-size: 10.5px; }
  .contact-list li { display: flex; align-items: center; gap: 6px; height: 17.5px; }
  .contact-list svg { width: 12px; height: 12px; fill: var(--brand-red); flex: none; }

  /* Back */
  .back-field {
    position: absolute; inset: 0;
    background: radial-gradient(ellipse at center, var(--brand-red-light) 0%, var(--brand-red) 75%);
  }
  .back-brand {
    position: absolute; left: 0; right: 0; top: 104px;
    text-align: center; color: var(--white);
  }
  .back-brand .brand-name { color: var(--white); }
  .back-brand .line-main { font-size: 38px; letter-spacing: 0.5px; }
  .back-brand .line-sub { font-size: 17px; margin-top: 0; }
  .back-url {
    margin-top: 6px;
    font-family: "Open Sans", sans-serif; font-style: italic;
    font-size: 10px; letter-spacing: 7.4px; color: var(--white);
  }
</style>
</head>
<body>
<div class="canvas">

  <section class="card card-front">
    <svg class="front-wave" viewBox="0 0 461 262" aria-hidden="true">
      <path d="M0 214 C 90 250, 180 262, 280 244 C 360 228, 420 228, 461 240 L461 246 C 420 236, 360 236, 280 252 C 180 268, 90 258, 0 222 Z" fill="var(--brand-gold)"/>
      <path d="M0 228 C 90 256, 180 264, 280 252 C 360 240, 420 236, 461 250 L461 262 L0 262 Z" fill="var(--brand-red)"/>
    </svg>

    <div class="brand-mark">
      <span class="brand-dot"></span>
      <span class="brand-name">
        <span class="line-main">HAVENPOINT</span>
        <span class="line-sub">SECURITY SYSTEMS INC.</span>
      </span>
    </div>

    <div class="divider"></div>

    <div class="contact">
      <div class="contact-name">Marcus Ellery</div>
      <div class="contact-title">CEO/Founder</div>
      <div class="contact-address">2140 Birchwood Court<br>Fairbanks, Alaska 99701</div>
      <ul class="contact-list">
        <li>
          <svg viewBox="0 0 24 24"><path d="M6.6 10.8a15.1 15.1 0 0 0 6.6 6.6l2.2-2.2a1 1 0 0 1 1-.25 11.4 11.4 0 0 0 3.6.57 1 1 0 0 1 1 1V20a1 1 0 0 1-1 1A17 17 0 0 1 3 4a1 1 0 0 1 1-1h3.5a1 1 0 0 1 1 1c0 1.25.2 2.45.57 3.57a1 1 0 0 1-.25 1z"/></svg>
          555 214 8830
        </li>
        <li>
          <svg viewBox="0 0 24 24"><path d="M7 1h10a2 2 0 0 1 2 2v18a2 2 0 0 1-2 2H7a2 2 0 0 1-2-2V3a2 2 0 0 1 2-2zm0 3v14h10V4z"/></svg>
          555 390 1746
        </li>
        <li>
          <svg viewBox="0 0 24 24"><path d="M2 5h20v14H2zm2 2v.5l8 5 8-5V7zm0 3v7h16v-7l-8 5z"/></svg>
          info@havenpoint.com
        </li>
        <li>
          <svg viewBox="0 0 24 24"><circle cx="12" cy="12" r="10"/><path d="M12 2v20M2 12h20" stroke="#fafafa" stroke-width="1.6"/></svg>
          www.havenpoint.com
        </li>
      </ul>
    </div>
  </section>

  <section class="card card-back">
    <div class="back-field" role="img" aria-label="Deep red background with a repeating brand pattern"></div>
    <div class="back-brand">
      <div class="brand-name">
        <span class="line-main">HAVENPOINT</span>
        <span class="line-sub">SECURITY SYSTEMS INC.</span>
      </div>
      <div class="back-url">www.havenpoint.com</div>
    </div>
  </section>

</div>
</body>
</html>
```